Ledgerwise Business Card Design

Business Card Design for new business called Ledgerwise focused on selling business software to small and medium size companies who have outgrown Tallyhouse. Similar companies would be Tallyhouse, Vemo, BrightCore. Also Dealharbor would be good to look at for additional ideas around look and feel.

Target Market(s)

Business to Business

Industry/Entity Type

Information Technology

Contact Information for Business Card

Standard Business Card Information

Font styles to use
Sans Serif

```html
<!DOCTYPE html>
<html lang="en">
<head>
<meta charset="utf-8">
<title>Ledgerwise Business Card</title>
<link href="https://fonts.googleapis.com/css2?family=Open+Sans:wght@400;600;700&display=swap" rel="stylesheet">
<style>
  :root {
    --blue: #1a6fae;
    --blue-deep: #0f5c99;
    --orange: #f2a82a;
    --ink: #3a3a3a;
    --paper: #ffffff;
    --backdrop: #e9e6e1;
  }
  html, body {
    margin: 0;
    padding: 0;
    width: 1200px;
    height: 892px;
    overflow: hidden;
    background: var(--backdrop);
    font-family: "Open Sans", Arial, sans-serif;
  }
  .canvas {
    position: relative;
    width: 1200px;
    height: 892px;
  }
  .card {
    position: absolute;
    left: 280px;
    width: 640px;
    height: 366px;
    background: var(--paper);
    box-shadow: 0 6px 18px rgba(0,0,0,0.18);
    overflow: hidden;
  }
  .card--front { top: 60px; }
  .card--back { top: 466px; }

  .card__band {
    position: absolute;
    inset: 0;
  }

  .brand {
    position: absolute;
    display: flex;
    align-items: center;
    gap: 12px;
  }
  .brand__dot {
    border-radius: 50%;
    background: var(--orange);
  }
  .brand__name {
    color: var(--blue);
    font-weight: 700;
    letter-spacing: 0.5px;
    text-transform: uppercase;
  }
  .card--front .brand { left: 196px; top: 58px; }
  .card--front .brand__dot { width: 34px; height: 34px; }
  .card--front .brand__name { font-size: 34px; }

  .card--back .brand {
    left: 50%;
    top: 50%;
    transform: translate(-50%, -50%);
    gap: 16px;
  }
  .card--back .brand__dot { width: 46px; height: 46px; }
  .card--back .brand__name { font-size: 46px; }

  .person {
    position: absolute;
    left: 40px;
    top: 150px;
  }
  .person__name {
    margin: 0;
    color: var(--blue);
    font-size: 27px;
    font-weight: 600;
    line-height: 1.1;
  }
  .person__role {
    margin: 2px 0 0;
    color: var(--ink);
    font-size: 15px;
  }

  .contacts {
    position: absolute;
    left: 40px;
    top: 220px;
    margin: 0;
    padding: 0;
    list-style: none;
    color: var(--ink);
    font-size: 15px;
    line-height: 24px;
  }
  .contacts__item {
    display: flex;
    align-items: center;
    gap: 10px;
  }
  .contacts__icon {
    width: 16px;
    height: 16px;
    flex: none;
  }
  .contacts__item--address {
    padding-left: 26px;
    font-size: 16px;
  }
</style>
</head>
<body>
<main class="canvas">

  <section class="card card--front" aria-label="Business card front">
    <svg class="card__band" width="640" height="366" viewBox="0 0 640 366" aria-hidden="true">
      <path d="M520 0 C 500 110, 470 170, 420 250 C 395 290, 392 330, 390 366 L 640 366 L 640 0 Z" fill="var(--orange)"/>
      <path d="M532 0 C 512 110, 484 172, 436 250 C 412 290, 408 330, 406 366 L 640 366 L 640 0 Z" fill="var(--blue-deep)"/>
    </svg>

    <div class="brand">
      <span class="brand__dot"></span>
      <span class="brand__name">Ledgerwise</span>
    </div>

    <div class="person">
      <h1 class="person__name">Corin Maddox</h1>
      <p class="person__role">Owner</p>
    </div>

    <ul class="contacts">
      <li class="contacts__item">
        <svg class="contacts__icon" viewBox="0 0 16 16" aria-hidden="true"><rect width="16" height="16" rx="3" fill="var(--blue)"/><rect x="5" y="3" width="6" height="10" rx="1" fill="none" stroke="#fff" stroke-width="1.4"/></svg>
        0400 318 274
      </li>
      <li class="contacts__item">
        <svg class="contacts__icon" viewBox="0 0 16 16" aria-hidden="true"><rect width="16" height="16" rx="3" fill="var(--blue)"/><path d="M4 4 L6.5 4 L7.5 6.5 L6 7.5 C6.8 9 7.5 9.7 8.5 10 L9.5 8.5 L12 9.5 L12 12 C7.5 12 4 8.5 4 4 Z" fill="#fff"/></svg>
        07 5550 0142
      </li>
      <li class="contacts__item">
        <svg class="contacts__icon" viewBox="0 0 16 16" aria-hidden="true"><rect width="16" height="16" rx="3" fill="var(--blue)"/><rect x="3" y="4.5" width="10" height="7" fill="none" stroke="#fff" stroke-width="1.3"/><path d="M3 4.5 L8 9 L13 4.5" fill="none" stroke="#fff" stroke-width="1.3"/></svg>
        hello@ledgerwise.com
      </li>
      <li class="contacts__item">
        <svg class="contacts__icon" viewBox="0 0 16 16" aria-hidden="true"><rect width="16" height="16" rx="3" fill="var(--blue)"/><circle cx="8" cy="8" r="4.5" fill="none" stroke="#fff" stroke-width="1.3"/><path d="M3.5 8 H12.5 M8 3.5 C6 6 6 10 8 12.5 M8 3.5 C10 6 10 10 8 12.5" fill="none" stroke="#fff" stroke-width="1"/></svg>
        www.ledgerwise.com
      </li>
      <li class="contacts__item contacts__item--address">42 Harbor Lane, Ste 3 Fairview, CO 80000</li>
    </ul>
  </section>

  <section class="card card--back" aria-label="Business card back">
    <div class="brand">
      <span class="brand__dot"></span>
      <span class="brand__name">Ledgerwise</span>
    </div>
  </section>

</main>
</body>
</html>
```